Fresh Dwelling Tract Hub needs a new Landing Page

I like to get a landing page or website with 2-3 pages to help target home buyers who are looking to buy homes from builders such as TQ Estates, Vostrum, P.J. Calloway, etc. The landing page/website to be non-cluttered and be able to explain to home buyers that there are many benefits to include me as their buyer's agent when they buy a brand new home from any builders.
I may want to incorporate a short explanation video (animated) on the landing page and then for the viewer to click on a button that will take them to another page where they can search for new homes from different builders.
Target Market(s)
Home buyers looking to buy brand new home from builders such as TQ Estates, Vostrum, P.J. Calloway, etc.
Industry/Entity Type
Real Estate
Number of Pages Required
2 page
Requirements
Must have
- The landing page may have the explanation video at the bottom of the landing page (scrolled down) or there may be a CALL TO ACTION button that takes the viewer to the 2nd page to watch the explanation video. Once they watched the explanation video and are still interested, they can click on another CALL TO ACTION button that will take them to another website that they will be able to search for all the available new homes and register their contact information.
Should not have
- No clutters and no dark colors.

```html
<!DOCTYPE html>
<html lang="en">
<head>
<meta charset="utf-8">
<title>Fresh Dwelling Tract Hub</title>
<link href="https://fonts.googleapis.com/css2?family=Open+Sans:wght@400;600&display=swap" rel="stylesheet">
<style>
  :root {
    --brand-green: #8abf6f;
    --button-green: #7dbd63;
    --label-green: #3d7a2b;
    --ink: #111111;
    --paper: #ffffff;
    --stone: #9a7a52;
    --stone-dark: #5e4a2f;
    --leaf: #4f7d34;
    --sky: #b9c9d8;
  }
  * { box-sizing: border-box; margin: 0; padding: 0; }
  html, body { width: 999px; height: 1200px; overflow: hidden; background: var(--paper); }
  body { font-family: "Open Sans", Arial, sans-serif; color: var(--ink); }
  .page { position: relative; width: 999px; height: 1200px; }

  .hero {
    position: absolute; left: 0; top: 0; width: 999px; height: 664px;
    background:
      linear-gradient(90deg, rgba(94,74,47,0.55) 0%, rgba(154,122,82,0.1) 35%, rgba(185,201,216,0.0) 50%, rgba(79,125,52,0.35) 70%, rgba(79,125,52,0.7) 100%),
      linear-gradient(180deg, var(--sky) 0%, #a99373 45%, var(--stone) 70%, #6f6a55 100%);
  }
  .brand-tag {
    position: absolute; left: 90px; top: 0; width: 160px; height: 82px;
    background: var(--brand-green);
    display: flex; align-items: center; justify-content: center; text-align: center;
    font-size: 11px; line-height: 15px; font-weight: 400; color: var(--ink); padding: 0 8px;
  }
  .play-button { position: absolute; left: 472px; top: 292px; width: 52px; height: 52px; }

  .intro {
    position: absolute; left: 60px; top: 706px; width: 879px;
    text-align: center; font-size: 18px; line-height: 23px;
  }
  .button {
    position: absolute; left: 358px; width: 281px; height: 58px;
    display: flex; align-items: center; justify-content: center;
    font-size: 17px; font-weight: 400; text-decoration: none;
  }
  .button-search { top: 813px; border: 2px solid var(--button-green); color: var(--label-green); }

  .contact-band {
    position: absolute; left: 0; top: 919px; width: 999px; height: 281px;
    background: var(--brand-green);
  }
  .contact-line {
    position: absolute; left: 0; top: 50px; width: 999px; text-align: center;
    font-size: 18px; line-height: 24px;
  }
  .button-contact { top: 116px; border: 2px solid var(--ink); color: var(--ink); }
  .rights { position: absolute; left: 24px; top: 225px; font-size: 12px; }
  .social { position: absolute; left: 840px; top: 213px; display: flex; gap: 17px; }
  .social span {
    width: 31px; height: 31px; border-radius: 50%;
    background: var(--ink); border: 2px solid var(--ink);
    box-shadow: inset 0 0 0 2px var(--brand-green);
  }
</style>
</head>
<body>
<main class="page">
  <section class="hero" role="img" aria-label="Photo of a sunlit stone village lane with ivy-covered walls, potted shrubs and cloudy sky">
    <div class="brand-tag">FRESH DWELLING TRACT HUB</div>
    <svg class="play-button" viewBox="0 0 52 52" aria-label="Play video">
      <circle cx="26" cy="26" r="24.5" fill="none" stroke="#111" stroke-width="2"/>
      <path d="M20 15 L37 26 L20 37 Z" fill="none" stroke="#111" stroke-width="2" stroke-linejoin="round"/>
    </svg>
  </section>

  <p class="intro">Lorem ipsum dolor sit amet, consectetur adipiscing elit. Sed id aliquam ligula. Morbi eget ornare nisi. Curabitur vel quam id urna aliquet facilisis. Nullam blandit pharetra mi sit amet finibus. Sed est enim, dignissim eget dapibus vel, aliquam eu ipsum.</p>

  <a class="button button-search" href="#">SEARCH</a>

  <footer class="contact-band">
    <p class="contact-line">Lorem ipsum dolor sit amet, consectetur adipiscing elit.</p>
    <a class="button button-contact" href="#">CONTACT US</a>
    <p class="rights">FRESH DWELLING TRACT HUB 2018 Rights</p>
    <div class="social" aria-label="Social links"><span></span><span></span><span></span></div>
  </footer>
</main>
</body>
</html>
```